Business Card Design

we are Marrowbank Farms & we would like a business card that stands out from the crowd and that we can apply this design to our products as we will be also placing orders for labels and stickers in the future

Industry/Entity Type

Business

Contact Information for Business Card

Packing Shed : 53 617 904
mobile : 0412 583 091
email : marrowbankfarms@kestrelnet.com
address : Copperbark Lane Tarrowin 4571

```html
<!DOCTYPE html>
<html lang="en">
<head>
<meta charset="utf-8">
<title>Marrowbank Farms – Business Card</title>
<link rel="stylesheet" href="https://fonts.googleapis.com/css2?family=Baloo+2:wght@700&family=Open+Sans:wght@400;600&display=swap">
<style>
  :root {
    --backdrop: #32322f;
    --card-white: #ffffff;
    --berry-red: #e41e26;
    --band-red: #ec1c24;
    --contact-text: #ffffff;
    --card-shadow: rgba(0, 0, 0, 0.45);
  }

  html, body {
    margin: 0;
    padding: 0;
    width: 1200px;
    height: 677px;
    overflow: hidden;
    background: var(--backdrop);
  }

  .canvas {
    position: relative;
    width: 1200px;
    height: 677px;
  }

  .card {
    position: absolute;
    top: 186px;
    width: 500px;
    height: 305px;
    background: var(--card-white);
    box-shadow: 0 10px 28px var(--card-shadow);
    overflow: hidden;
  }

  .card--front { left: 60px; }
  .card--back  { left: 640px; }

  .brand {
    display: flex;
    align-items: center;
    gap: 14px;
    font-family: "Baloo 2", "Trebuchet MS", sans-serif;
    font-weight: 700;
    color: var(--berry-red);
    line-height: 1;
  }

  .brand__mark {
    flex: none;
    border-radius: 50%;
    background: var(--berry-red);
  }

  .card--front .brand {
    position: absolute;
    left: 0;
    right: 0;
    top: 120px;
    justify-content: center;
    font-size: 34px;
  }

  .card--front .brand__mark {
    width: 58px;
    height: 58px;
  }

  .card--back .brand {
    position: absolute;
    left: 36px;
    top: 58px;
    font-size: 27px;
  }

  .card--back .brand__mark {
    width: 52px;
    height: 52px;
  }

  .contact-band {
    position: absolute;
    left: 0;
    right: 0;
    bottom: 0;
    height: 124px;
    background: var(--band-red);
    padding: 20px 0 0 28px;
    box-sizing: border-box;
  }

  .contact-list {
    margin: 0;
    display: grid;
    grid-template-columns: 84px auto;
    row-gap: 3px;
    font-family: "Open Sans", Arial, sans-serif;
    font-size: 12.5px;
    color: var(--contact-text);
  }

  .contact-list dt { font-weight: 400; }
  .contact-list dd { margin: 0; font-weight: 600; }
</style>
</head>
<body>
<main class="canvas">
  <section class="card card--front" aria-label="Business card front">
    <div class="brand">
      <span class="brand__mark"></span>
      <span class="brand__name">Marrowbank Farms</span>
    </div>
  </section>

  <section class="card card--back" aria-label="Business card back">
    <div class="brand">
      <span class="brand__mark"></span>
      <span class="brand__name">Marrowbank Farms</span>
    </div>
    <div class="contact-band">
      <dl class="contact-list">
        <dt>Packing Shed</dt><dd>: 53 617 904</dd>
        <dt>Mobile</dt><dd>: 0412 583 091</dd>
        <dt>Email</dt><dd>: marrowbankfarms@kestrelnet.com</dd>
        <dt>Address</dt><dd>: Copperbark Lane Tarrowin 4571</dd>
      </dl>
    </div>
  </section>
</main>
</body>
</html>
```